Law Firm Needs Brochure Redesign Using New Logo

We are a personal injury law firm that does auto injuries and other personal injury cases. We want a new brochure that has our updated logo and information. Instead of gold and black, we want more navy, as matches the new logo. The Auto Liability portion should read: "(required by the state of Arizona in the amounts of $25,000 per person / $50,000 per accident, but a higher amount may be best )." The other information can remain the same. We'd like the brochure to keep the same professional tone as the previous brochure.
Our website is https://www.marbrenlegal.com/.

```html
<!DOCTYPE html>
<html lang="en">
<head>
<meta charset="utf-8">
<title>Marbren Legal – Car Accident Brochure</title>
<link href="https://fonts.googleapis.com/css2?family=Montserrat:wght@500;600;700;800&family=Open+Sans:wght@400;600;700&display=swap" rel="stylesheet">
<style>
  :root{
    --navy:#1b2440;
    --navy-deep:#141b33;
    --navy-soft:#2b3656;
    --ink:#1d2238;
    --muted:#5d6478;
    --paper:#ffffff;
    --mist:#eef0f4;
    --stage:#e4e5e8;
    --line:#c9ced9;
  }
  *{box-sizing:border-box;margin:0;padding:0}
  html,body{width:851px;height:1200px;overflow:hidden}
  body{background:var(--stage);font-family:"Open Sans",Arial,sans-serif;color:var(--ink);position:relative}
  .sheet{position:absolute;left:30px;width:791px;height:545px;display:flex;background:var(--paper);box-shadow:0 4px 14px rgba(20,27,51,.18)}
  .sheet--outside{top:30px}
  .sheet--inside{top:622px}
  .panel{width:263.67px;height:100%;position:relative;overflow:hidden}
  .panel+.panel{border-left:1px solid #e3e5eb}
  h2,h3,.brand,.stat-num{font-family:"Montserrat",Arial,sans-serif}

  /* brand lockup */
  .brand{display:flex;align-items:center;gap:8px;font-weight:800;font-size:17px;letter-spacing:.06em;color:var(--navy)}
  .brand::before{content:"";width:14px;height:14px;background:currentColor;display:block}
  .brand--light{color:var(--paper)}

  /* outside: stats */
  .stats{background:var(--navy-deep);color:var(--paper);padding:34px 26px;display:flex;flex-direction:column}
  .stat-label{font-size:17px;font-weight:600}
  .stat-num{font-size:42px;font-weight:800;line-height:1}
  .stat-text{font-size:10.5px;line-height:1.45;margin-top:8px;color:#c9cfe0}
  .stat+.stat{margin-top:40px}
  .stats .note{margin-top:auto;font-size:8px;line-height:1.5;color:#aab2c8}
  .stats .brand{margin-top:16px}

  /* outside: contact */
  .contact{display:flex;flex-direction:column;align-items:center;padding:0 24px 36px;text-align:center}
  .contact-block{margin-top:118px;font-size:9.5px;line-height:1.6;color:var(--muted)}
  .contact-block h3{font-size:11px;color:var(--ink);letter-spacing:.08em;margin-bottom:4px}
  .contact-block .gap{margin-top:10px}
  .contact .brand{margin-top:auto}

  /* outside: cover */
  .cover{display:flex;flex-direction:column}
  .cover-head{background:var(--navy);color:var(--paper);padding:22px 22px 20px}
  .cover-head h2{font-size:14.5px;font-weight:800;line-height:1.3;letter-spacing:.02em}
  .cover-head p{font-size:11px;margin-top:6px;color:#d3d8e6}
  .cover-photo{height:300px;background:radial-gradient(ellipse at 65% 45%,#6c7180 0%,#2b2f3a 45%,#0c0e13 100%)}
  .cover-foot{flex:1;display:flex;align-items:center;justify-content:center}

  /* inside: tips */
  .tips{padding:26px 20px}
  .tips h2{font-size:13px;font-weight:800;color:var(--navy);letter-spacing:.02em;margin-bottom:10px}
  .tips ol{list-style:none;counter-reset:tip}
  .tips li{counter-increment:tip;font-size:8.3px;line-height:1.42;color:var(--muted);padding-left:14px;position:relative;margin-bottom:6px}
  .tips li::before{content:counter(tip)".";position:absolute;left:0;font-weight:700;color:var(--navy)}
  .tips li b{color:var(--ink);font-weight:700;text-transform:uppercase}

  /* inside: coverage */
  .coverage{background:var(--navy);color:var(--paper);display:flex;flex-direction:column}
  .coverage-photo{height:150px;background:linear-gradient(160deg,#c8ccd6 0%,#8e95a6 55%,#3d4560 100%)}
  .coverage h2{font-size:13px;font-weight:800;text-align:center;padding:12px 10px;background:var(--navy-soft);letter-spacing:.03em}
  .coverage .lead{font-size:8.5px;line-height:1.45;padding:12px 20px 4px;color:#cdd3e3}
  .cover-item{font-size:8.3px;line-height:1.45;padding:7px 20px;color:#cdd3e3;border-bottom:1px solid rgba(255,255,255,.14)}
  .cover-item b{color:var(--paper);font-weight:700}

  /* inside: behavior */
  .behavior{display:flex;flex-direction:column}
  .behavior-top{background:var(--navy);color:var(--paper);padding:24px 22px 18px}
  .behavior-top h2{font-size:15px;font-weight:800;letter-spacing:.03em;margin-bottom:10px}
  .behavior-top h3{font-size:10px;font-weight:800;margin-top:8px;letter-spacing:.03em}
  .behavior-top h3.big{font-size:13px}
  .behavior-top p{font-size:8.3px;line-height:1.45;color:#cdd3e3;margin-top:3px}
  .behavior-photo{height:200px;background:linear-gradient(140deg,#d9dbe0 0%,#9aa0ad 50%,#4a5064 100%)}
  .behavior-foot{flex:1;display:flex;align-items:center;justify-content:center}
</style>
</head>
<body>

<section class="sheet sheet--outside">
  <div class="panel stats">
    <div class="stat">
      <div class="stat-label">over</div>
      <div class="stat-num">107,000</div>
      <p class="stat-text">crashes will happen in the state of Arizona this year.</p>
    </div>
    <div class="stat">
      <div class="stat-label">over</div>
      <div class="stat-num">700</div>
      <p class="stat-text">of those will result in fatalities.</p>
    </div>
    <p class="note">If you have been injured in a crash, our team is ready to review your case, explain your options and help you move forward with confidence.</p>
    <div class="brand brand--light">MARBREN LEGAL</div>
  </div>

  <div class="panel contact">
    <div class="contact-block">
      <h3>CONTACT US</h3>
      <p>Marbren Legal Group</p>
      <p class="gap">2140 E Camelback Rd<br>Suite 310<br>Phoenix, AZ 85016</p>
      <p class="gap">(602) 555-0148<br>www.marbrenlegal.com</p>
    </div>
    <div class="brand">MARBREN LEGAL</div>
  </div>

  <div class="panel cover">
    <div class="cover-head">
      <h2>PROTECT YOUR FAMILY IN CASE OF A CAR ACCIDENT</h2>
      <p>A little knowledge and preparation go a long way</p>
    </div>
    <div class="cover-photo" role="img" aria-label="Front of a dark modern car with headlight lit, in low light"></div>
    <div class="cover-foot"><div class="brand">MARBREN LEGAL</div></div>
  </div>
</section>

<section class="sheet sheet--inside">
  <div class="panel tips">
    <h2>TOP 10 TIPS TO AVOID A CRASH</h2>
    <ol>
      <li><b>Anyone making a left turn</b> must wait for all oncoming traffic to clear before proceeding.</li>
      <li><b>When your light turns green,</b> check for other vehicles before entering the intersection.</li>
      <li><b>Allow plenty of room</b> between you and the car in front of you.</li>
      <li><b>Avoid being distracted.</b> Put away phones, food and anything that pulls your eyes off the road.</li>
      <li><b>Keep the volume of your radio</b> down and never wear headphones.</li>
      <li><b>Be especially careful</b> on the weekends and early mornings.</li>
      <li><b>Don't speed.</b> Speed is a factor in many crashes in Arizona.</li>
      <li><b>Don't drink and drive.</b> Plan a safe ride home before you go out.</li>
      <li><b>Use your turn signals.</b> Let other drivers know your next move.</li>
      <li><b>Stay rested.</b> Pull over if you feel drowsy behind the wheel.</li>
    </ol>
  </div>

  <div class="panel coverage">
    <div class="coverage-photo" role="img" aria-label="Hands holding a small toy car, symbolizing insurance protection"></div>
    <h2>HAVE THE RIGHT COVERAGE</h2>
    <p class="lead">Many people don't know about the different kinds of insurance available. In addition to liability, you may want:</p>
    <p class="cover-item"><b>AUTO LIABILITY</b> (required by the state of Arizona in the amounts of $25,000 per person / $50,000 per accident, but a higher amount may be best).</p>
    <p class="cover-item"><b>UNINSURED OR UNDERINSURED MOTORIST COVERAGE</b> protects you if the other driver has little or no insurance.</p>
    <p class="cover-item"><b>MEDICAL PAYMENTS COVERAGE</b> helps pay medical bills for you and your passengers after a crash.</p>
    <p class="cover-item"><b>COMPREHENSIVE / COLLISION</b> pays to repair or replace your own vehicle.</p>
  </div>

  <div class="panel behavior">
    <div class="behavior-top">
      <h2>MODEL SAFE BEHAVIOR</h2>
      <h3>ALWAYS BUCKLE UP.</h3>
      <p>Make sure every passenger is properly restrained before you start the car.</p>
      <h3 class="big">NEVER TEXT WHILE DRIVING</h3>
      <p>Studies show texting drivers are far more likely to crash. Show your children that no text is more important than their safety.</p>
    </div>
    <div class="behavior-photo" role="img" aria-label="Child safety seat fastened in the back seat of a car"></div>
    <div class="behavior-foot"><div class="brand">MARBREN LEGAL</div></div>
  </div>
</section>

</body>
</html>
```